Cover and label for Christian CD with lively original music for kids

The album title is Hope Runs Wide. It's for children, but is also designed to be enjoyable for older members of the family to listen to. The final cover should reflect the over-arching theme of God's love from a Christian perspective. If it depicts children, It should be culturally and racially inclusive. It should evoke feelings of warmth, joy and belonging (or at least openness) for viewers. And it should appeal to kids and adults. There should be some bright color but no overwhelmingly "loud" designs please. Album title and artist name should be clear-Hope Runs Wide and Miss Tilda respectively (may need flexibility on artist name as that has not been finalized). Label should be adapted from or complementary to cover art.

Industry/Entity Type

Christian

```html
<!DOCTYPE html>
<html lang="en">
<head>
<meta charset="utf-8">
<title>Hope Runs Wide – Cover and Disc Label</title>
<link href="https://fonts.googleapis.com/css2?family=Amatic+SC:wght@700&family=Open+Sans:wght@400;600&display=swap" rel="stylesheet">
<style>
  :root {
    --page: #f4f5f5;
    --sky-deep: #3fb3c4;
    --sky-mid: #6cc6d0;
    --sky-light: #a9dde1;
    --cloud: #d8eff0;
    --ink-white: #ffffff;
    --ink-dark: #1f3d44;
    --hub-silver: #d9dcdd;
    --hub-shine: #f7f8f8;
    --hub-edge: #9aa3a6;
  }
  * { margin: 0; padding: 0; box-sizing: border-box; }
  html, body {
    width: 1200px; height: 878px; overflow: hidden;
    background: var(--page);
  }
  .canvas {
    position: relative; width: 1200px; height: 878px;
    font-family: "Open Sans", Arial, sans-serif;
  }
  .cover {
    position: absolute; left: 30px; top: 159px;
    width: 560px; height: 560px; overflow: hidden;
    box-shadow: 0 6px 18px rgba(0,0,0,0.12);
  }
  .cover-sky {
    position: absolute; inset: 0;
    background:
      radial-gradient(ellipse 40% 22% at 35% 42%, var(--cloud) 0%, transparent 70%),
      radial-gradient(ellipse 45% 20% at 30% 80%, rgba(216,239,240,0.7) 0%, transparent 70%),
      linear-gradient(160deg, var(--sky-mid) 0%, var(--sky-deep) 55%, var(--sky-mid) 100%);
  }
  .cover-title {
    position: absolute; right: 48px; bottom: 56px;
    font-family: "Amatic SC", "Comic Sans MS", cursive;
    font-weight: 700; font-size: 64px; line-height: 0.82;
    color: var(--ink-white); text-align: left;
  }
  .cover-title span { display: block; }
  .cover-title .indent { padding-left: 34px; }
  .disc {
    position: absolute; left: 620px; top: 164px;
    width: 550px; height: 550px;
    filter: drop-shadow(0 6px 14px rgba(0,0,0,0.15));
  }
  .disc-artist {
    font-family: "Open Sans", Arial, sans-serif; font-size: 15px;
    letter-spacing: 14px; fill: var(--ink-dark);
  }
  .disc-rim-text {
    font-family: "Open Sans", Arial, sans-serif; font-size: 11.5px;
    fill: var(--ink-dark);
  }
  .disc-format {
    font-family: "Open Sans", Arial, sans-serif; font-weight: 600;
    font-size: 13px; fill: var(--ink-dark);
  }
  .disc-title {
    font-family: "Amatic SC", "Comic Sans MS", cursive;
    font-weight: 700; font-size: 50px; fill: var(--ink-white);
  }
</style>
</head>
<body>
<main class="canvas">
  <section class="cover">
    <div class="cover-sky" role="img" aria-label="Soft turquoise sky with drifting white clouds"></div>
    <h1 class="cover-title"><span>Hope</span><span class="indent">Runs Wide</span></h1>
  </section>

  <svg class="disc" viewBox="0 0 550 550" aria-label="Disc label">
    <defs>
      <linearGradient id="disc-sky" x1="0" y1="0" x2="1" y2="1">
        <stop offset="0" stop-color="#a9dde1"/>
        <stop offset="0.5" stop-color="#7ccbd3"/>
        <stop offset="1" stop-color="#5cbcc8"/>
      </linearGradient>
      <radialGradient id="hub-metal" cx="0.5" cy="0.5" r="0.5">
        <stop offset="0.3" stop-color="#f7f8f8"/>
        <stop offset="0.8" stop-color="#d9dcdd"/>
        <stop offset="1" stop-color="#9aa3a6"/>
      </radialGradient>
      <path id="rim-path" d="M 275,275 m -252,0 a 252,252 0 1,0 504,0 a 252,252 0 1,0 -504,0"/>
    </defs>
    <circle class="disc-art" cx="275" cy="275" r="275" fill="url(#disc-sky)" role="img" aria-label="Turquoise sky with soft clouds"/>
    <circle cx="275" cy="275" r="100" fill="#bfe6e8"/>
    <circle cx="275" cy="275" r="88" fill="url(#hub-metal)"/>
    <circle cx="275" cy="275" r="55" fill="var(--hub-shine)" stroke="var(--hub-edge)" stroke-width="1"/>
    <circle cx="275" cy="275" r="18" fill="var(--page)" stroke="var(--hub-edge)" stroke-width="1"/>
    <text class="disc-rim-text">
      <textPath href="#rim-path" startOffset="2%">Copyright © 2014 All rights reserved.  Any unauthorized duplication is strictly prohibited.   Copyright © 2014 All rights reserved.  Any unauthorized duplication is strictly prohibited.</textPath>
    </text>
    <text class="disc-artist" x="70" y="150" transform="rotate(-30 70 150)">MISS TILDA</text>
    <rect x="86" y="232" width="10" height="10" fill="var(--ink-dark)"/>
    <text class="disc-format" x="102" y="242">Sound Disc</text>
    <text class="disc-title" x="310" y="408">Hope</text>
    <text class="disc-title" x="270" y="450">Runs Wide</text>
  </svg>
</main>
</body>
</html>
```